Online Music Gear Store needs Business Cards

We need BC designs for our e-commerce for meetings and networking
we are an Online Store and we sell Audio and Music Equipment and Gear
we also provide EVENTUAL Audio and Music Production services but our core service is the Online Store: Selling Premium Brands

we are based in Tijuana and San Diego CA.
our brand/name is: Reelnook

our name comes from the early tape machines that the Marlowes and many other early day artist used to record with to do their magnificent masterpieces.

Now in 2014 we can have Amazing Studio-Quality Multitrack sessions with a few pieces of Gear and an Slatebook... For example, you can only have your Tovaphone and an Quenra Pairline to start recording using Shedmix for Vexor OS.

If the best bands from the early days had to use million dollar recording studios with very expensive gear such as 4-track tape machines... now you can achieve better sounding results in your bedroom, using the gear we sell.

Thats what we try to Communicate with the Name:

That you... a young musician can start doing multitrack sessions using the Best Gear with the Latest Technology and compatible with Zelbooks, Vexor OS devices:

Example of the Premium Brands we sell are:
Quenra, RJ Sonicworks

we want to communicate (even if we are an ecommerce and a startup) that we are Serious, and Very Elegant, Sophisticated and Minimal.

that we provide Complete solutions, the best gear... the best brands... that we also do our productions with the best gear, best brands and very important we are Pearwood ONLY, Zelbooks Only

examples of the brands we sell are Volkmarsen, Quenra, RJ Sonicworks, Olin Marsh Instruments, Arc 9. Our focus is Music Technology.
we also use Tempra Studio Z.

Our favorite colors are black, white, grey, silver, orange, blue, green, maybe bit of yellow.

No need to use all of them but you can combine. At the end you can use Color Theory to achieve assertive communication.

Target Market(s)

CEO's, VP's, VC's, Sales People, High Class executives...
Purchasing Departments, and Corporations.

Industry/Entity Type

E-Commerce

Requirements
Must have
• Should include:

1. Logo
2. website,
3. Managing Director Info:
4. Minimal and Elegant/Upper Class

feel free to suggest ideas, feel free to play around with logo and fonts as well... since we are not 100% happy with our logo...

must also show that we are Pearwood and Zelbook only in a way without being obvious or without showing Pearwood Logo

we need to have at the end of the project the .AI
.PSD and any related designed file to edit in the future, logo, numbers, etc...

my info:

Tomas Elias Barrera-Fuentes
Reelnook | Mexico City, Tijuana, San Diego,
Friendwall | Chirplet | Searchly+ | Clipboardia | Snapgrid ???? (what do you thing about this links ???) too much ???
Mobile: +5216647390418 | 0115216647390418
USA Number: 1-800-555-0173
VidLink & QuickNote: music@reelnook-example.mx
Callwave: musicreelnookmx
Should not have
• it shouldn't use our real address, but should imply that we are in Mexico City, in Tijuana and San Diego CA.

Should not use the Pearwood Logo (even if we are Pearwood only)

should not have Robotix or PC/Panesoft related designs.

```html
<!DOCTYPE html>
<html lang="en">
<head>
<meta charset="utf-8">
<title>Reelnook Business Card</title>
<link rel="stylesheet" href="https://fonts.googleapis.com/css2?family=Exo+2:wght@400;600&family=Source+Sans+3:wght@400;600&display=swap">
<style>
  :root {
    --backdrop: #3b3b3d;
    --card-dark: #231f20;
    --card-light: #ffffff;
    --accent-blue: #29b6e8;
    --ink: #231f20;
    --ink-soft: #3a3a3a;
    --dot-grey: #4a4748;
  }
  * { box-sizing: border-box; margin: 0; padding: 0; }
  html, body { width: 1200px; height: 900px; overflow: hidden; }
  body {
    background: var(--backdrop);
    position: relative;
    font-family: "Source Sans 3", sans-serif;
  }
  .card {
    position: absolute;
    top: 297px;
    width: 530px;
    height: 306px;
    border-radius: 26px;
    overflow: hidden;
  }
  /* Front */
  .card-front { left: 55px; background: var(--card-dark); }
  .halftone-field {
    position: absolute; inset: 0;
    background:
      radial-gradient(ellipse 45% 55% at 10% 35%, rgba(90,86,88,0.55), transparent 70%),
      radial-gradient(ellipse 40% 50% at 92% 70%, rgba(90,86,88,0.5), transparent 70%),
      radial-gradient(ellipse 60% 35% at 50% 95%, rgba(80,76,78,0.45), transparent 70%);
  }
  .front-wordmark {
    position: absolute; left: 0; right: 0; top: 168px;
    display: flex; justify-content: center; align-items: center; gap: 12px;
  }
  .brand-dot {
    width: 22px; height: 22px; border-radius: 50%;
    background: var(--accent-blue);
  }
  .brand-name {
    font-family: "Exo 2", sans-serif;
    font-weight: 600;
    font-size: 34px;
    letter-spacing: 1px;
    line-height: 1;
  }
  .front-wordmark .brand-name { color: #ffffff; }
  .front-tagline {
    position: absolute; left: 0; right: 0; top: 258px;
    text-align: center;
    font-family: "Exo 2", sans-serif;
    font-size: 16px;
    color: var(--accent-blue);
    letter-spacing: 0.3px;
  }
  /* Back */
  .card-back { left: 615px; background: var(--card-light); }
  .contact-block { position: absolute; left: 35px; top: 36px; width: 210px; }
  .person-name { color: var(--accent-blue); font-weight: 600; font-size: 15px; line-height: 1.2; }
  .person-role { color: var(--ink); font-size: 15px; line-height: 1.25; }
  .divider { height: 1px; background: var(--accent-blue); width: 185px; margin: 11px 0 13px; }
  .contact-list { list-style: none; font-size: 14.5px; color: var(--ink); line-height: 1.3; }
  .contact-list li { display: flex; align-items: center; gap: 7px; }
  .contact-list li.no-icon { padding-left: 17px; }
  .contact-list.spaced { margin-top: 12px; }
  .contact-list svg { width: 10px; height: 10px; flex: none; fill: var(--accent-blue); }
  .back-tagline {
    font-family: "Exo 2", sans-serif;
    font-size: 13px; line-height: 1.2; color: var(--ink);
  }
  .back-wordmark {
    position: absolute; right: 34px; top: 250px;
    display: flex; align-items: center; gap: 10px;
  }
  .back-wordmark .brand-dot { background: var(--accent-blue); width: 20px; height: 20px; }
  .back-wordmark .brand-name { color: var(--ink); font-size: 28px; }
</style>
</head>
<body>

<section class="card card-front">
  <div class="halftone-field" role="img" aria-label="Grey halftone dot pattern sweeping across the card"></div>
  <div class="front-wordmark">
    <span class="brand-dot"></span>
    <span class="brand-name">Reelnook</span>
  </div>
  <p class="front-tagline">Recording Gear &amp; Music Production</p>
</section>

<section class="card card-back">
  <div class="contact-block">
    <p class="person-name">Tomas Elias Barrera-Fuentes</p>
    <p class="person-role">managing director</p>
    <div class="divider"></div>
    <ul class="contact-list">
      <li><svg viewBox="0 0 10 10"><rect x="2.5" y="0" width="5" height="10" rx="1"/><rect x="3.5" y="1.2" width="3" height="6.3" fill="#fff"/></svg>5216 647 390 418</li>
      <li class="no-icon">0115 216 647 390 418</li>
      <li><svg viewBox="0 0 10 10"><path d="M2 0.5 L4 2.8 L3 4 Q4.5 6 6 7 L7.2 6 L9.5 8 L8 9.7 Q3.5 9 0.3 2 Z"/></svg>1-800-555-0173 (USA)</li>
    </ul>
    <ul class="contact-list spaced">
      <li><svg viewBox="0 0 10 10"><rect x="0" y="2" width="10" height="6.5"/><path d="M0 2 L5 5.8 L10 2" stroke="#fff" stroke-width="0.9" fill="none"/></svg>music@reelnook-example.mx</li>
      <li><svg viewBox="0 0 10 10"><circle cx="5" cy="5" r="5"/><circle cx="5" cy="5" r="2" fill="#fff"/></svg>musicreelnookmx</li>
      <li><svg viewBox="0 0 10 10"><circle cx="5" cy="5" r="4.5" fill="none" stroke="#29b6e8" stroke-width="1"/><ellipse cx="5" cy="5" rx="2" ry="4.5" fill="none" stroke="#29b6e8" stroke-width="0.8"/><line x1="0.5" y1="5" x2="9.5" y2="5" stroke="#29b6e8" stroke-width="0.8"/></svg>www.reelnook-example.mx</li>
    </ul>
    <div class="divider"></div>
    <p class="back-tagline">Recording Gear<br>&amp; Music Production</p>
  </div>
  <div class="back-wordmark">
    <span class="brand-dot"></span>
    <span class="brand-name">Reelnook</span>
  </div>
</section>

</body>
</html>
```